Financial Consulting Company in need of technical diagram

Attached is a basic template to follow, however the following changes must be made:
- Get rid of reflection boxes at the bottom
-Delete anything in parentheses
-Change top box to read "Uncover Value Opportunities"
-Change bottom right box to read "Sales and Operations Planning"
-Change bottom left box to read "Financial Planning"

Additionally we would like to see something a little more creative and cohesive. One possibility is using "Cheveron" type arrows to show the "wheel" effect.

Please email tmorven@brightlake7.example if you have any questions!
Updates

Please see newly uploaded image for an example of how we would like it re-created.

Industry/Entity Type

Financial

Requirements
Must have
• I'm looking for something that keeps the "wheel" approach, but is not a direct re-creation of the example given. The boxes for example, dont' necessarily need to stay boxes. Feel free to play around with placement as well.
Nice to have
• Please see green wheel for example of how it can be re-created.

```html
<!DOCTYPE html>
<html lang="en">
<head>
<meta charset="utf-8">
<title>Value Cycle Wheel</title>
<link rel="stylesheet" href="https://fonts.googleapis.com/css2?family=Didact+Gothic&display=swap">
<style>
  :root {
    --wheel-green: #55cd7a;
    --paper: #ffffff;
  }
  html, body {
    margin: 0;
    padding: 0;
    width: 1200px;
    height: 900px;
    overflow: hidden;
    background: var(--paper);
  }
  .wheel {
    display: block;
    width: 1200px;
    height: 900px;
  }
  .wheel-band {
    fill: none;
    stroke: var(--wheel-green);
    stroke-width: 135;
  }
  .stage-disc {
    fill: var(--wheel-green);
  }
  .stage-gap {
    fill: none;
    stroke: var(--paper);
    stroke-width: 8;
    stroke-linecap: round;
  }
  .stage-tail {
    fill: none;
    stroke: var(--wheel-green);
    stroke-width: 9;
    stroke-linecap: round;
  }
  .flow-arrow {
    fill: var(--paper);
    stroke: var(--paper);
    stroke-width: 12;
    stroke-linejoin: round;
  }
  .stage-label {
    font-family: "Didact Gothic", "Century Gothic", sans-serif;
    font-size: 24px;
    fill: var(--paper);
    text-anchor: middle;
  }
</style>
</head>
<body>
<svg class="wheel" viewBox="0 0 1200 900" xmlns="http://www.w3.org/2000/svg" role="img" aria-label="Five-stage value cycle wheel">
  <!-- Ring band -->
  <circle class="wheel-band" cx="630" cy="440" r="305"/>

  <!-- Stage: Uncover Value Opportunities -->
  <g class="stage">
    <circle class="stage-tail" cx="537" cy="140" r="126" pathLength="100" stroke-dasharray="34 66" transform="rotate(100 537 140)"/>
    <circle class="stage-gap" cx="537" cy="140" r="116" pathLength="100" stroke-dasharray="38 62" transform="rotate(95 537 140)"/>
    <circle class="stage-disc" cx="537" cy="140" r="110"/>
    <text class="stage-label" x="537" y="116">
      <tspan x="537" dy="0">Uncover</tspan>
      <tspan x="537" dy="30">Value</tspan>
      <tspan x="537" dy="30">Opportunities</tspan>
    </text>
  </g>

  <!-- Stage: Strategize and Align -->
  <g class="stage">
    <circle class="stage-tail" cx="878" cy="253" r="126" pathLength="100" stroke-dasharray="34 66" transform="rotate(172 878 253)"/>
    <circle class="stage-gap" cx="878" cy="253" r="116" pathLength="100" stroke-dasharray="38 62" transform="rotate(167 878 253)"/>
    <circle class="stage-disc" cx="878" cy="253" r="110"/>
    <text class="stage-label" x="878" y="232">
      <tspan x="878" dy="0">Strategize</tspan>
      <tspan x="878" dy="30">and</tspan>
      <tspan x="878" dy="30">Align</tspan>
    </text>
  </g>

  <!-- Stage: Sales and Operations Planning -->
  <g class="stage">
    <circle class="stage-tail" cx="880" cy="622" r="126" pathLength="100" stroke-dasharray="34 66" transform="rotate(244 880 622)"/>
    <circle class="stage-gap" cx="880" cy="622" r="116" pathLength="100" stroke-dasharray="38 62" transform="rotate(239 880 622)"/>
    <circle class="stage-disc" cx="880" cy="622" r="108"/>
    <text class="stage-label" x="880" y="600">
      <tspan x="880" dy="0">Sales and</tspan>
      <tspan x="880" dy="30">Operations</tspan>
      <tspan x="880" dy="30">Planning</tspan>
    </text>
  </g>

  <!-- Stage: Financial Planning -->
  <g class="stage">
    <circle class="stage-tail" cx="535" cy="742" r="126" pathLength="100" stroke-dasharray="34 66" transform="rotate(316 535 742)"/>
    <circle class="stage-gap" cx="535" cy="742" r="116" pathLength="100" stroke-dasharray="38 62" transform="rotate(311 535 742)"/>
    <circle class="stage-disc" cx="535" cy="742" r="110"/>
    <text class="stage-label" x="535" y="726">
      <tspan x="535" dy="0">Financial</tspan>
      <tspan x="535" dy="30">Planning</tspan>
    </text>
  </g>

  <!-- Stage: Assess the Results -->
  <g class="stage">
    <circle class="stage-tail" cx="322" cy="443" r="126" pathLength="100" stroke-dasharray="34 66" transform="rotate(28 322 443)"/>
    <circle class="stage-gap" cx="322" cy="443" r="116" pathLength="100" stroke-dasharray="38 62" transform="rotate(23 322 443)"/>
    <circle class="stage-disc" cx="322" cy="443" r="110"/>
    <text class="stage-label" x="322" y="436">
      <tspan x="322" dy="0">Assess the</tspan>
      <tspan x="322" dy="30">Results</tspan>
    </text>
  </g>

  <!-- Flow arrows (clockwise) -->
  <g class="flow-arrows">
    <g transform="rotate(-72 630 440) translate(935 440) rotate(90)">
      <path class="flow-arrow" d="M-24,-28 L30,0 L-24,28 Z"/>
    </g>
    <g transform="rotate(0 630 440) translate(935 440) rotate(90)">
      <path class="flow-arrow" d="M-24,-28 L30,0 L-24,28 Z"/>
    </g>
    <g transform="rotate(72 630 440) translate(935 440) rotate(90)">
      <path class="flow-arrow" d="M-24,-28 L30,0 L-24,28 Z"/>
    </g>
    <g transform="rotate(144 630 440) translate(935 440) rotate(90)">
      <path class="flow-arrow" d="M-24,-28 L30,0 L-24,28 Z"/>
    </g>
    <g transform="rotate(216 630 440) translate(935 440) rotate(90)">
      <path class="flow-arrow" d="M-24,-28 L30,0 L-24,28 Z"/>
    </g>
  </g>
</svg>
</body>
</html>
```